BPRV Postcard Design: Mosquito Control, Lawn Maintenance and Pressure washing

I have a new company based in Atlanta,Georgia named Brightwell Pest Relief Ventures, LLC. We specializes in Mosquito Control. We also have additional services: Lawn maintenance, Pressure Washing and Gutter Cleaning. I would like to see designs with the colors Black, Red, Gray. We would like the customer to think of us when it comes to Enjoying a mosquito free yard and improving the look and feel of their home and lawn.

Industry/Entity Type

It Company

Requirements
Nice to have
• Treatment plans starting at $69/mt - front of card
• The additional services we offer - back of card.

```html
<!DOCTYPE html>
<html lang="en">
<head>
<meta charset="utf-8">
<title>Brightwell Pest Relief Ventures – Postcard</title>
<link href="https://fonts.googleapis.com/css2?family=Exo+2:ital,wght@0,600;0,700;0,800;1,700;1,800;1,900&family=Russo+One&family=Saira+Condensed:wght@700&display=swap" rel="stylesheet">
<style>
  :root {
    --bg: #ecebe8;
    --black: #1a1a1a;
    --black-soft: #262626;
    --red: #c8161d;
    --red-deep: #9c1016;
    --white: #ffffff;
    --paper: #f6f6f6;
    --paper-alt: #fbfbfb;
    --ink: #222222;
    --gray: #8f8f8f;
  }
  * { box-sizing: border-box; margin: 0; padding: 0; }
  html, body { width: 1200px; height: 1000px; overflow: hidden; }
  body { background: var(--bg); position: relative; font-family: "Exo 2", sans-serif; }

  .card { position: absolute; width: 690px; height: 460px; overflow: hidden; box-shadow: 0 6px 18px rgba(0,0,0,.25); }

  /* Front */
  .card--front { left: 40px; top: 30px; background: var(--black); }
  .front__band { position: absolute; left: 0; right: 0; top: 250px; height: 165px; background: linear-gradient(180deg, var(--red) 0%, var(--red-deep) 100%); }
  .front__name { position: absolute; left: 60px; right: 20px; top: 18px; text-align: center; font-family: "Russo One", sans-serif; font-size: 70px; line-height: 1; color: var(--red); }
  .front__tagline { position: absolute; left: 60px; right: 20px; top: 100px; text-align: center; font-family: "Saira Condensed", sans-serif; font-weight: 700; font-size: 36px; line-height: 1; color: var(--white); }
  .front__phone { position: absolute; left: 60px; right: 20px; top: 150px; text-align: center; font-family: "Exo 2", sans-serif; font-weight: 800; font-size: 62px; letter-spacing: 2px; line-height: 1; color: var(--red); }
  .front__offer { position: absolute; left: 30px; top: 262px; color: var(--white); font-style: italic; font-weight: 900; }
  .front__offer-line { font-size: 34px; line-height: 1.05; }
  .front__offer-price { font-size: 66px; line-height: 1.05; margin-top: 2px; }
  .front__web { position: absolute; left: 30px; top: 420px; font-style: italic; font-weight: 700; font-size: 21px; color: var(--white); letter-spacing: .5px; }
  .front__badge { position: absolute; left: 415px; top: 205px; width: 240px; height: 240px; }

  /* Back */
  .card--back { left: 470px; top: 510px; background: var(--paper-alt); }
  .back__panel { position: absolute; left: 0; top: 0; width: 395px; height: 100%; background: var(--paper); }
  .back__return { position: absolute; left: 26px; top: 14px; font-family: Arial, Helvetica, sans-serif; font-size: 12px; line-height: 1.25; color: var(--ink); }
  .back__name { position: absolute; left: 26px; width: 360px; top: 64px; text-align: center; font-family: "Russo One", sans-serif; font-size: 52px; line-height: 1; color: var(--red); }
  .back__tagline { position: absolute; left: 26px; width: 360px; top: 122px; text-align: center; font-family: "Saira Condensed", sans-serif; font-weight: 700; font-size: 27px; line-height: 1; color: var(--ink); }
  .back__photo { position: absolute; border: 3px solid var(--white); box-shadow: 0 2px 5px rgba(0,0,0,.3); }
  .back__photo--lawn { left: 40px; top: 168px; width: 148px; height: 100px; background: linear-gradient(160deg, #5b7a3a, #3f5e28 60%, #b8262a); }
  .back__photo--wash { left: 40px; top: 278px; width: 150px; height: 100px; background: linear-gradient(170deg, #7d8a6a, #8e9190 55%, #5d6261); }
  .back__photo--gutter { left: 198px; top: 278px; width: 150px; height: 100px; background: linear-gradient(160deg, #2f3a4a, #6b5a2e 60%, #a9882f); }
  .back__services { position: absolute; left: 198px; top: 168px; list-style: none; font-style: italic; font-weight: 800; font-size: 21px; line-height: 1.27; color: var(--ink); }
  .back__services li::before { content: "•"; color: var(--red); margin-right: 6px; font-style: normal; }
  .back__cta { position: absolute; left: 40px; top: 388px; font-style: italic; font-weight: 800; font-size: 19px; line-height: 1.1; color: var(--ink); }
  .back__phone { position: absolute; left: 38px; top: 426px; font-weight: 800; font-size: 30px; letter-spacing: 1px; line-height: 1; color: var(--red); }
</style>
</head>
<body>

<section class="card card--front" aria-label="Postcard front">
  <div class="front__band"></div>
  <h1 class="front__name">Brightwell</h1>
  <p class="front__tagline">Pest Relief Ventures LLC</p>
  <p class="front__phone">404-555-0187</p>
  <div class="front__offer">
    <p class="front__offer-line">Treatment plans</p>
    <p class="front__offer-line">starting at</p>
    <p class="front__offer-price">$69/mt</p>
  </div>
  <p class="front__web">www.brightwellpestrelief.com</p>

  <svg class="front__badge" viewBox="0 0 240 240" aria-hidden="false">
    <defs>
      <radialGradient id="badge-photo" cx="50%" cy="45%" r="60%">
        <stop offset="0%" stop-color="#e8e8e8"/>
        <stop offset="100%" stop-color="#9a9a9a"/>
      </radialGradient>
      <path id="badge-arc" d="M 38 150 A 86 86 0 1 1 202 150"/>
    </defs>
    <circle cx="120" cy="120" r="118" fill="var(--red)" stroke="var(--black)" stroke-width="3"/>
    <circle cx="120" cy="120" r="88" fill="url(#badge-photo)" role="img" aria-label="Close-up photo of a mosquito on skin"/>
    <line x1="58" y1="58" x2="182" y2="182" stroke="var(--red)" stroke-width="20"/>
    <circle cx="120" cy="120" r="88" fill="none" stroke="var(--red)" stroke-width="14"/>
    <text font-family="'Exo 2', sans-serif" font-weight="800" font-style="italic" font-size="17" fill="var(--white)">
      <textPath href="#badge-arc" startOffset="50%" text-anchor="middle">Enjoy a mosquito free yard!</textPath>
    </text>
  </svg>
</section>

<section class="card card--back" aria-label="Postcard back">
  <div class="back__panel"></div>
  <address class="back__return">
    Brightwell Pest Relief Ventures<br>
    4812 Larkspur Rd. Suite 210<br>
    Marietta, GA 30060
  </address>
  <h2 class="back__name">Brightwell</h2>
  <p class="back__tagline">Pest Relief Ventures LLC</p>

  <div class="back__photo back__photo--lawn" role="img" aria-label="Photo of a red lawn mower on green grass"></div>
  <div class="back__photo back__photo--wash" role="img" aria-label="Photo of a patio being pressure washed"></div>
  <div class="back__photo back__photo--gutter" role="img" aria-label="Photo of leaves being cleared from a gutter"></div>

  <ul class="back__services">
    <li>Mosquito Control</li>
    <li>Lawn Maintenance</li>
    <li>Pressure Washing</li>
    <li>Gutter Cleaning</li>
  </ul>

  <p class="back__cta">Call Us Today<br>for An Estimate!</p>
  <p class="back__phone">404-555-0187</p>
</section>

</body>
</html>
```